Attic Rivers (Progressive House Album)

Hey Guys,

I'm a music artist and I need a CD Cover done for my new album.The album is called "Attic Rivers" and I really need something artistic, almost like a painting that reflects the name of the album.

Also please feel free to step out from the whole "almost like a painting" box, if your inner creator has something else to say. But preferably I'd have it as a painting...

Here are some keywords: Deep, Progressive, Lucid Dreaming, Attic Rivers...

Please listen to the 3:30 demo of the album to get a better idea.

Thanks,

RoJa

Update:

I've uploaded a few images to kinda help you with the mood/colour tone and direction of what I want, Also, the script writing (I've uploaded a few examples), do it in white colour (left to right, going little bit upwards), preferably on the bottom of the image, simple, one touch, thin hand writing. Have it fading in size (bigger to smaller) as you get to the end of each word. Just like when you sign something, but have it written in two lines.

The whole image should be deep in colour with sort of a glow effect.

Must have
• Name of the album with Script writing,
Should not have
• No paper mosaic art. Image pieced together with cut outs from different sources.

```html
<!DOCTYPE html>
<html lang="en">
<head>
<meta charset="utf-8">
<title>Attic Rivers – RoJa – Album Cover Presentation</title>
<link href="https://fonts.googleapis.com/css2?family=Sacramento&family=Pinyon+Script&display=swap" rel="stylesheet">
<style>
  :root {
    --paper: #ffffff;
    --ink-blue: #1a4a88;
    --rule: #d9d9d9;
    --ocean-deep: #0a0f2e;
    --ocean-mid: #1a3f8f;
    --ocean-glow: #38a8e8;
    --wash: #e6e8ee;
    --wash-deep: #c9ccd8;
    --specimen-ink: #6a6d76;
    --white: #ffffff;
    --disc-hub: #efefef;
    --disc-ring: #b8b8b8;
  }
  * { margin: 0; padding: 0; box-sizing: border-box; }
  html, body { width: 1200px; height: 848px; overflow: hidden; background: var(--paper); }
  .sheet { position: relative; width: 1200px; height: 848px; background: var(--paper); }

  .header-title {
    position: absolute; left: 0; width: 1200px; top: 138px; text-align: center;
    font-family: "Sacramento", cursive; font-size: 58px; line-height: 1;
    color: var(--ink-blue); letter-spacing: -1px;
  }
  .header-artist {
    position: absolute; left: 668px; top: 196px;
    font-family: "Sacramento", cursive; font-size: 36px; line-height: 1; color: var(--ink-blue);
  }
  .rule {
    position: absolute; left: 115px; width: 965px; height: 3px; border-radius: 2px;
    background: linear-gradient(90deg, transparent, var(--rule) 15%, var(--rule) 85%, transparent);
  }
  .rule--top { top: 241px; }
  .rule--bottom { top: 698px; }

  .panel { position: absolute; top: 298px; width: 356px; height: 334px; overflow: hidden; }

  .type-specimen { left: 52px; }
  .type-specimen__wash {
    position: absolute; inset: 0;
    background: radial-gradient(ellipse at 50% 40%, var(--wash) 0%, var(--wash-deep) 100%);
  }
  .type-specimen__text {
    position: absolute; left: 0; right: 0; top: 86px; text-align: center;
    font-family: "Pinyon Script", cursive; color: var(--specimen-ink);
    font-size: 18px; line-height: 22px;
  }
  .type-specimen__name { display: block; font-size: 44px; line-height: 52px; margin-bottom: 2px; }

  .cover-front { left: 449px; }
  .ocean-art {
    position: absolute; inset: 0;
    background:
      radial-gradient(ellipse 30% 55% at 48% 62%, var(--ocean-glow) 0%, rgba(56,168,232,0.35) 45%, transparent 80%),
      radial-gradient(ellipse at 50% 50%, var(--ocean-mid) 0%, var(--ocean-deep) 85%);
  }
  .cover-front__notch { position: absolute; left: 305px; top: 115px; }
  .cover-title {
    position: absolute; left: 82px; top: 258px;
    font-family: "Sacramento", cursive; font-size: 44px; line-height: 1; color: var(--white);
    transform: rotate(-3deg);
  }
  .cover-artist {
    position: absolute; left: 238px; top: 292px;
    font-family: "Sacramento", cursive; font-size: 26px; line-height: 1; color: var(--white);
  }

  .disc { position: absolute; left: 829px; top: 304px; width: 322px; height: 322px; }
  .disc__title {
    position: absolute; left: 68px; top: 222px;
    font-family: "Sacramento", cursive; font-size: 40px; line-height: 1; color: var(--white);
    transform: rotate(-3deg);
  }
  .disc__artist {
    position: absolute; left: 224px; top: 253px;
    font-family: "Sacramento", cursive; font-size: 24px; line-height: 1; color: var(--white);
  }
</style>
</head>
<body>
<main class="sheet">
  <h1 class="header-title">Attic Rivers</h1>
  <p class="header-artist">RoJa</p>
  <div class="rule rule--top"></div>

  <section class="panel type-specimen">
    <div class="type-specimen__wash" role="img" aria-label="Faded underwater painting with jellyfish and coral, washed out in pale grey"></div>
    <p class="type-specimen__text">
      <span class="type-specimen__name">Copperplate</span>
      often called script,<br>
      originally written with feather quill,<br>
      derives its name from an engraving style<br>
      popular in the seventeenth century.<br>
      ABCDEFGHIJKLMNOPQRSTUVWXYZ
    </p>
  </section>

  <section class="panel cover-front">
    <div class="ocean-art" role="img" aria-label="Deep blue underwater painting with glowing jellyfish, fish and coral around a bright central light"></div>
    <svg class="cover-front__notch" width="104" height="104" viewBox="0 0 104 104" aria-hidden="true">
      <circle cx="52" cy="52" r="52" fill="var(--paper)"/>
    </svg>
    <p class="cover-title">Attic Rivers</p>
    <p class="cover-artist">RoJa</p>
  </section>

  <div class="disc">
    <svg width="322" height="322" viewBox="0 0 322 322">
      <defs>
        <radialGradient id="disc-ocean" cx="45%" cy="55%" r="60%">
          <stop offset="0" stop-color="#38a8e8"/>
          <stop offset="0.35" stop-color="#1a3f8f"/>
          <stop offset="1" stop-color="#0a0f2e"/>
        </radialGradient>
      </defs>
      <circle cx="161" cy="161" r="161" fill="url(#disc-ocean)" role="img" aria-label="Disc face printed with the same underwater jellyfish painting"/>
      <circle cx="161" cy="161" r="47" fill="var(--paper)"/>
      <circle cx="161" cy="161" r="30" fill="var(--disc-hub)" stroke="var(--disc-ring)" stroke-width="2"/>
      <circle cx="161" cy="161" r="24" fill="none" stroke="var(--disc-ring)" stroke-width="1"/>
    </svg>
    <p class="disc__title">Attic Rivers</p>
    <p class="disc__artist">RoJa</p>
  </div>

  <div class="rule rule--bottom"></div>
</main>
</body>
</html>
```